Fiber Optic Internet flyer promotion Winter 2016-2017

I am looking for a marketing flyer that will not be folded, single sided that will advertise a Fiber Optic internet promotion that we are currently running.

The design should be clean, flow well, quickly grab attention, and if a very few short seconds list what the promotion is, and direct them to contact us.

It needs to list a few features of the promotion, but does not need to be in this order and should flow well with the flyer
1.) Fiber Optic Internet
2.) 100 Mbits for $140 /month or 150 Mbits for $190 /month
3.) Free construction cost up to $10,000, limited funds available.
4.) Limited time offer. Must commit before funds run out.

(555) 274-3916, www.kelvoranet.example

Target Market(s)

Small to large business

Industry/Entity Type

Internet Service Provider

Requirements
Must have
• Eye catching appeal. Quickly convey the message of the promotion and our company name and phone number.
Should not have
• Our company is primarily a wireless ISP. This promotion is all about Fiber Optic. I do not want to draw attention to the "wireless" portion of our business with this flyer.

```html
<!DOCTYPE html>
<html lang="en">
<head>
<meta charset="UTF-8">
<title>Fiber Optic Internet Flyer</title>
<link href="https://fonts.googleapis.com/css2?family=Lato:ital,wght@0,400;0,700;0,900;1,400&display=swap" rel="stylesheet">
<style>
  :root {
    --page-bg: #ffffff;
    --flyer-dark: #151515;
    --flyer-navy: #12203f;
    --brand-red: #d42535;
    --brand-blue: #0c2a8e;
    --footer-navy: #14296b;
    --text-light: #ffffff;
    --photo-dark: #1d2430;
    --photo-mid: #2b4a86;
    --photo-light: #8a8f96;
  }
  * { margin: 0; padding: 0; box-sizing: border-box; }
  html, body {
    width: 1200px; height: 1200px; overflow: hidden;
    background: var(--page-bg);
    font-family: "Lato", Arial, sans-serif;
  }
  .flyer {
    position: absolute; left: 289px; top: 160px;
    width: 622px; height: 880px;
    background: var(--page-bg);
    overflow: hidden;
  }
  .hero {
    position: absolute; left: 0; top: 0; width: 100%; height: 425px;
    background: linear-gradient(to bottom, var(--flyer-dark) 0%, var(--flyer-dark) 62%, var(--flyer-navy) 100%);
    text-align: center;
  }
  .headline {
    position: absolute; left: 0; width: 100%;
    font-weight: 900; line-height: 1; letter-spacing: -1px;
  }
  .headline--fiber { top: 44px; font-size: 92px; color: var(--brand-red); }
  .headline--internet { top: 128px; font-size: 92px; color: var(--brand-blue); }
  .price {
    position: absolute; left: 0; width: 100%;
    font-size: 39px; font-weight: 700; color: var(--brand-red); line-height: 1;
  }
  .price--basic { top: 222px; }
  .price--plus { top: 276px; }
  .offer-title {
    position: absolute; left: 0; width: 100%; top: 336px;
    font-size: 25px; font-weight: 900; color: var(--text-light); line-height: 1;
  }
  .offer-note {
    position: absolute; left: 0; width: 100%; top: 367px;
    font-size: 19px; color: var(--text-light); line-height: 1;
  }
  .offer-fine {
    position: absolute; left: 0; width: 100%; top: 394px;
    font-size: 19px; font-style: italic; color: var(--text-light); line-height: 1;
  }
  .photo {
    position: absolute; left: 0; top: 425px; width: 100%; height: 307px;
    background: linear-gradient(100deg, var(--photo-light) 0%, var(--photo-dark) 45%, var(--photo-mid) 100%);
    border-bottom: 3px solid var(--footer-navy);
  }
  .footer {
    position: absolute; left: 0; top: 732px; width: 100%; height: 148px;
    background: var(--page-bg);
  }
  .brand {
    position: absolute; left: 30px; top: 58px;
    display: flex; align-items: center; gap: 10px;
  }
  .brand-dot {
    width: 26px; height: 26px; border-radius: 50%;
    background: var(--brand-red);
  }
  .brand-name {
    font-size: 28px; font-weight: 900; color: var(--footer-navy); line-height: 1;
  }
  .contact {
    position: absolute; right: 25px; top: 16px; text-align: right;
  }
  .contact-cta {
    font-size: 24px; font-weight: 700; color: var(--footer-navy); line-height: 1;
  }
  .contact-phone {
    margin-top: 12px;
    font-size: 41px; font-weight: 900; color: var(--brand-red); line-height: 1;
  }
  .contact-web {
    margin-top: 8px;
    font-size: 22px; color: var(--footer-navy); line-height: 1; letter-spacing: 0.5px;
  }
</style>
</head>
<body>
  <div class="flyer">
    <section class="hero">
      <div class="headline headline--fiber">FIBER OPTIC</div>
      <div class="headline headline--internet">INTERNET</div>
      <div class="price price--basic">100 Mbits for $140 /month or</div>
      <div class="price price--plus">150 Mbits for $190 /month</div>
      <div class="offer-title">LIMITED TIME OFFER</div>
      <div class="offer-note">Must commit before funds run out</div>
      <div class="offer-fine">Free construction cost up to $10,000, limited funds available.</div>
    </section>
    <div class="photo" role="img" aria-label="Technician in a white shirt using a tablet beside server racks with colorful fiber cables"></div>
    <footer class="footer">
      <div class="brand">
        <span class="brand-dot"></span>
        <span class="brand-name">Kelvora Networks</span>
      </div>
      <div class="contact">
        <div class="contact-cta">Get It Today! Call Us</div>
        <div class="contact-phone">(555) 274-3916</div>
        <div class="contact-web">www.kelvoranet.example</div>
      </div>
    </footer>
  </div>
</body>
</html>
```